Business Consulting Company requires a website design (PSD+HTML+CSS required)

Marlowe Advisory is a Business Consulting Company that provides Analysis, Business Coaching and Systems and Document Design for clients.

We would like a simplistic yet professional looking website design that uses high quality imagery to project a professional persona across our entire site.

The completed project will need to include PSD files (for editing in Photoshop) and will need to also include HTML+CSS coded files that can be edited in Adobe Dreamweaver CS5.5.

Marlowe Advisory currently has a functioning website (located at www.marloweadvisory-example.com.au) but would like to replace its current site with something more professional, user friendly and content simplistic, with the overall design of this project being clean and very easy to navigate whilst remaining professionally focused.

A brief has been attached to this project to provide the key details but please feel free to contact me if you require any clarification or have any questions regarding the project.

Target Market(s)

The target audience for this website will be small to medium sized businesses (of all descriptions).

Industry/Entity Type

Business

Coding

Coded - Design and coding required

Number of Pages Required

5+ page

Requirements
Must have
• Simplistic design structure
• Professional images
• Easy to navigate
• Must be uploaded in PSD format
• Must be coded (HTML+CSS) and compatible with Adobe Dreamweaver CS5.5
Nice to have
• Use of the Company’s corporate colours throughout the site design
• Adding a Home page slider bar with images and short catchy messages (i.e. text based statements)
• Having a quick link box on each page that provides easy navigation throughout the site
• The use of different icons and images to depict our different services (i.e. a different icon and image for analysis service and coaching service etc.).
• All pages should follow a similar theme (universal approach to all pages)
Should not have
• When coding, images should not be used in place of text (all text must be editable)

```html
<!DOCTYPE html>
<html lang="en">
<head>
<meta charset="utf-8">
<title>Marlowe Advisory</title>
<link href="https://fonts.googleapis.com/css2?family=Arimo:wght@400;700&family=Open+Sans:wght@300;400&display=swap" rel="stylesheet">
<style>
:root{
  --blue:#0097d7;
  --blue-bright:#0aa0e0;
  --slate:#5c5d60;
  --slate-dark:#4f5053;
  --charcoal:#3f4043;
  --ink:#333;
  --muted:#a9abae;
  --white:#fff;
  --rule:#d8d8d8;
}
*{margin:0;padding:0;box-sizing:border-box}
html,body{width:785px;height:1200px;overflow:hidden}
body{position:relative;font-family:"Arimo",Arial,sans-serif;color:var(--ink);background:var(--white);font-size:8px;line-height:1.35}
.abs{position:absolute}

/* header */
.site-header{left:0;top:0;width:785px;height:34px;background:var(--white)}
.brand{left:105px;top:5px;display:flex;align-items:center;gap:6px}
.brand-dot{width:22px;height:22px;border-radius:50%;background:var(--blue)}
.brand-name{font-size:15px;letter-spacing:2px;color:#555;font-weight:400}
.contact-bar{left:478px;top:11px;display:flex;align-items:center;gap:6px;font-size:9px;color:#555;white-space:nowrap}
.follow{left:560px;top:11px;font-size:9px;letter-spacing:1px;color:#555;white-space:nowrap}
.social-sq{top:5px;width:21px;height:21px}
.social-a{left:632px;background:#3b5998}
.social-b{left:661px;background:#2aa7e0}

.main-nav{left:0;top:34px;width:785px;height:21px;background:#f1f1f1;border-top:1px solid var(--rule);border-bottom:1px solid var(--rule)}
.main-nav ul{list-style:none;position:absolute;left:105px;top:0;display:flex;height:20px}
.main-nav li{padding:0 11px;line-height:20px;font-size:7px;text-transform:uppercase;color:#333}
.main-nav li.active{background:#4e4f52;color:var(--blue-bright);padding:0 16px}
.search-icon{left:658px;top:36px}

/* hero */
.hero{left:0;top:55px;width:785px;height:248px;background:linear-gradient(110deg,#1d3c63 0%,#5a86b0 35%,#c9d6e2 55%,#8fa8c3 75%,#27466d 100%)}
.hero-title{left:105px;top:131px;color:var(--white);font-size:17px;font-weight:700;letter-spacing:.3px}
.hero-text{left:105px;top:162px;width:330px;color:var(--white);font-size:8px;line-height:1.35}
.hero-btn{left:105px;top:207px;width:92px;height:20px;border:1px solid var(--blue-bright);color:var(--white);font-size:7px;line-height:18px;text-align:center;text-transform:uppercase}

/* why */
.why{left:0;top:303px;width:785px;height:273px;background:var(--slate)}
.section-title{width:785px;left:0;text-align:center;color:var(--white);font-family:"Open Sans",Arial,sans-serif;font-weight:400;font-size:24px;letter-spacing:.5px}
.why-title{top:330px}
.why-intro{left:162px;top:366px;width:460px;text-align:center;color:var(--white);font-size:8px}
.service{width:260px;display:flex;gap:14px}
.service-icon{flex:0 0 31px;height:31px;border:2px solid var(--white);border-radius:50%;display:flex;align-items:center;justify-content:center}
.service h3{color:var(--white);font-size:8.5px;font-weight:700;margin:2px 0 6px}
.service p{color:var(--muted);font-size:7.5px;line-height:1.35}
.s1{left:109px;top:427px}.s2{left:397px;top:427px}
.s3{left:109px;top:491px}.s4{left:397px;top:491px}

/* about */
.about{left:0;top:576px;width:785px;height:176px;background:var(--white)}
.col-head{color:var(--blue);font-size:9px;font-weight:700}
.team-head{left:109px;top:591px}
.welcome-head{left:254px;top:591px}
.team-photo{left:109px;top:604px;width:131px;height:66px;background:linear-gradient(90deg,#c9b9a4,#e8e2d8,#b8a792)}
.welcome-photo{left:254px;top:604px;width:138px;height:116px;background:linear-gradient(160deg,#5f8fc0,#2f5e95 60%,#1e3e6b)}
.team-text{left:109px;top:681px;width:130px;font-size:8px;color:#444}
.welcome-text{left:408px;top:604px;width:272px;font-size:8px;color:#444}
.welcome-text p{margin-bottom:9px}

/* testimonials */
.testimonials{left:0;top:752px;width:785px;height:185px;background:var(--blue)}
.testimonials-title{top:787px;font-weight:300;font-size:30px}
.avatar{left:233px;top:832px;width:48px;height:48px;border-radius:50%;background:linear-gradient(#f2f2f2,#d9d4cf);border:2px solid var(--white)}
.quote{left:300px;top:832px;width:300px;color:var(--white);font-size:9px;line-height:1.3}
.quote q{font-weight:700;quotes:none}
.quote .mark{font-size:12px;font-weight:700;margin-right:3px}
.quote cite{display:block;font-style:italic;font-size:8px;margin-left:10px}
.dots{left:380px;top:893px;display:flex;gap:4px}
.dots span{width:5px;height:5px;border-radius:50%;background:var(--white)}
.dots span.on{background:#d33}

/* footer */
.site-footer{left:0;top:937px;width:785px;height:240px;background:var(--slate)}
.news-title{left:0;top:1020px;width:785px;text-align:center;color:var(--white);font-size:15px}
.news-input{left:262px;top:1042px;width:183px;height:24px;background:var(--slate-dark);color:#ddd;font-size:8px;line-height:24px;padding-left:12px}
.news-btn{left:453px;top:1042px;width:71px;height:24px;border:1px solid var(--blue-bright);color:var(--blue-bright);font-size:7px;font-weight:700;line-height:22px;text-align:center;text-transform:uppercase}
.foot-col{color:var(--white);font-size:7px;line-height:1.2}
.foot-col h4{font-weight:400;font-size:9.5px;margin-bottom:6px}
.foot-col ul{list-style:none}
.foot-menu{left:109px;top:1112px}
.foot-services{left:255px;top:1112px}
.foot-circle{top:1113px;width:17px;height:17px;border:1px solid #ccc;border-radius:50%}
.fc1{left:563px}.fc2{left:589px}
.foot-contact{left:540px;top:1136px;color:var(--white);font-size:6.5px;white-space:nowrap}
.foot-contact .phone{color:var(--blue-bright);font-size:11px;font-weight:700;letter-spacing:.5px}
.copyright{left:0;top:1177px;width:785px;height:23px;background:var(--charcoal);color:#8a8b8e;font-size:6px;text-align:center;line-height:23px}
</style>
</head>
<body>

<header class="site-header abs">
  <div class="brand abs"><span class="brand-dot"></span><span class="brand-name">MARLOWE ADVISORY</span></div>
  <div class="contact-bar abs">
    <svg width="11" height="11" viewBox="0 0 24 24"><path d="M6.6 10.8a15.1 15.1 0 0 0 6.6 6.6l2.2-2.2c.3-.3.7-.4 1-.2 1.1.4 2.3.6 3.6.6.6 0 1 .4 1 1V20c0 .6-.4 1-1 1A17 17 0 0 1 3 4c0-.6.4-1 1-1h3.5c.6 0 1 .4 1 1 0 1.3.2 2.5.6 3.6.1.3 0 .7-.2 1z" fill="#666"/></svg>
    <span>03 9000 4821</span>
  </div>
  <div class="follow abs">FOLLOW US:</div>
  <div class="social-sq social-a abs"></div>
  <div class="social-sq social-b abs"></div>
</header>

<nav class="main-nav abs">
  <ul>
    <li class="active">Home</li>
    <li>About Us</li>
    <li>Services &#9662;</li>
    <li>Contact Us</li>
    <li>Testimonials</li>
  </ul>
</nav>
<svg class="search-icon abs" width="16" height="16" viewBox="0 0 16 16"><circle cx="6.5" cy="6.5" r="4.5" fill="none" stroke="#444" stroke-width="1.8"/><line x1="10" y1="10" x2="14.5" y2="14.5" stroke="#444" stroke-width="2"/></svg>

<section class="hero abs" role="img" aria-label="Business people reviewing documents at a desk with coffee and a tablet"></section>
<h1 class="hero-title abs">WE TAKE THE PAIN OUT OF BUSINESS</h1>
<p class="hero-text abs">Understanding that every situation is different and that every one of our client's is unique we tailor make all our business development services packages to suit our clients individual business needs.</p>
<div class="hero-btn abs">Click to read more</div>

<section class="why abs"></section>
<h2 class="section-title why-title abs">WHY JOIN MARLOWE</h2>
<p class="why-intro abs">What makes Marlowe Advisory so unique is our unequivocal passion for helping others succeed. We understand and embrace the fact that our success is based upon the success of our partners and that without them, we have no real purpose for existing.</p>

<div class="service s1 abs">
  <div class="service-icon"><svg width="14" height="14" viewBox="0 0 14 14"><rect x="1" y="8" width="3" height="5" fill="#fff"/><rect x="5.5" y="5" width="3" height="8" fill="#fff"/><rect x="10" y="2" width="3" height="11" fill="#fff"/></svg></div>
  <div><h3>Business Analysis</h3><p>With this in mind, each of our services can be undertaken as a single entity or may be combined to formulate a specific package that's right for your business.</p></div>
</div>
<div class="service s2 abs">
  <div class="service-icon"><svg width="14" height="14" viewBox="0 0 14 14"><circle cx="7" cy="4" r="2.5" fill="#fff"/><rect x="4" y="7.5" width="6" height="6" rx="1" fill="#fff"/></svg></div>
  <div><h3>Business Coaching</h3><p>With this in mind, each of our services can be undertaken as a single entity or may be combined to formulate a specific package that's right for your business.</p></div>
</div>
<div class="service s3 abs">
  <div class="service-icon"><svg width="14" height="14" viewBox="0 0 14 14"><rect x="2.5" y="1" width="9" height="12" fill="none" stroke="#fff" stroke-width="1.5"/><line x1="4.5" y1="5" x2="9.5" y2="5" stroke="#fff"/><line x1="4.5" y1="8" x2="9.5" y2="8" stroke="#fff"/></svg></div>
  <div><h3>Business Systems and Document Creation</h3><p>With this in mind, each of our services can be undertaken as a single entity or may be combined to formulate a specific package that's right for your business.</p></div>
</div>
<div class="service s4 abs">
  <div class="service-icon"><svg width="14" height="14" viewBox="0 0 14 14"><rect x="2" y="3" width="5" height="10" fill="#fff"/><rect x="8" y="6" width="4" height="7" fill="#fff"/></svg></div>
  <div><h3>New Business Start-up Packages</h3><p>With this in mind, each of our services can be undertaken as a single entity or may be combined to formulate a specific package that's right for your business.</p></div>
</div>

<section class="about abs"></section>
<h3 class="col-head team-head abs">Our team</h3>
<h3 class="col-head welcome-head abs">Welcome to Marlowe Advisory</h3>
<div class="team-photo abs" role="img" aria-label="Group of smiling business team members"></div>
<div class="welcome-photo abs" role="img" aria-label="Business meeting with company name shown on a screen"></div>
<p class="team-text abs">Marlowe Advisory is a business analysis, coaching and business development provider who specialises in assisting businesses to achieve maximum efficiency, increased</p>
<div class="welcome-text abs">
  <p>Marlowe Advisory is a business analysis, coaching and business development provider who specialises in assisting businesses to achieve maximum efficiency, increased productivity and who can assist with improving a business's overall profitability.</p>
  <p>At Marlowe, we pride ourselves on our ability to form strong client relationships whilst delivering impressive results. For us, it's all about effective communication coupled with practical and measurable results!</p>
  <p>who specialises in assisting businesses to achieve maximum efficiency, increased productivity and who can assist with improving a business's overall profitability.</p>
</div>

<section class="testimonials abs"></section>
<h2 class="section-title testimonials-title abs">WHAT THEY SAY</h2>
<div class="avatar abs" role="img" aria-label="Portrait of a smiling client"></div>
<blockquote class="quote abs">
  <span class="mark">&ldquo;</span><q>Lorem ipsum dolor sit amet, consectetur adipiscing elit. Ut rutrum elit in arcu blandit, eget pretium nisl accumsan. Sed ultricies commodo tortor, eu pretium mauris.</q>
  <cite>- Someone famous</cite>
</blockquote>
<div class="dots abs"><span class="on"></span><span></span><span></span></div>

<footer class="site-footer abs"></footer>
<p class="news-title abs">Subscribe to our Newsletter for latest news.</p>
<div class="news-input abs">Your Email</div>
<div class="news-btn abs">Subscribe</div>
<div class="foot-col foot-menu abs">
  <h4>MENU</h4>
  <ul><li>Home</li><li>About Us</li><li>Services</li><li>Contact Us</li><li>Testimonials</li></ul>
</div>
<div class="foot-col foot-services abs">
  <h4>SERVICES</h4>
  <ul><li>Business Analysis</li><li>Business Coaching</li><li>Business Systems and Document Creation</li><li>New Business Start-up Packages</li></ul>
</div>
<div class="foot-circle fc1 abs"></div>
<div class="foot-circle fc2 abs"></div>
<div class="foot-contact abs">
  <div class="phone">(03) 9000 4821</div>
  <div>Mon - Fri | 9.00AM - 06.00PM</div>
  <div>Questions? admin@marloweadvisory-example.com.au</div>
</div>
<div class="copyright abs">&copy; Copyright 2014 Marlowe Advisory</div>

</body>
</html>
```